Electrical Automation Controls Distributor needs updated business cards

We are a 25 year old electrical wholesaler of high quality, technically advanced automation controls for industry. We are based on Long Island NY and have sales offices in Philadelphia and Massachusetts. The markets serve include, Power Generation, Transportation and Rail, OEM, Semiconductor, LED, MRO, Packaging and Aerospace. We are certified, WBE. DBE, TRAMLIC, KVT4417 and QR5583.
Our Colors are royal blue and goldish yellow...and we like simple clean designs....not too busy . I've attached a sample of our existing card and our line card.

```html
<!DOCTYPE html>
<html lang="en">
<head>
<meta charset="utf-8">
<title>Brightline Controls – Business Card</title>
<link href="https://fonts.googleapis.com/css2?family=Lato:wght@400;700&display=swap" rel="stylesheet">
<style>
  :root {
    --page-bg: #e9e7e3;
    --band-navy: #363b6e;
    --panel-royal: #2d3a9c;
    --card-royal: #2c39a6;
    --card-royal-light: #3747b8;
    --gold: #f2b632;
    --white: #ffffff;
    --muted-link: #7d86c4;
    --rule: rgba(255, 255, 255, 0.28);
  }
  * { box-sizing: border-box; margin: 0; padding: 0; }
  html, body {
    width: 1200px; height: 900px; overflow: hidden;
    background: var(--page-bg);
    font-family: "Lato", sans-serif;
  }
  .canvas { position: relative; width: 1200px; height: 900px; }
  .card {
    position: absolute; left: 260px;
    width: 680px; height: 390px;
    overflow: hidden;
    box-shadow: 0 6px 18px rgba(0, 0, 0, 0.18);
  }
  /* Front */
  .card--front { top: 45px; background: var(--band-navy); }
  .front-panel {
    position: absolute; top: 0; bottom: 0; left: 200px; width: 280px;
    background: var(--panel-royal);
    display: flex; flex-direction: column; align-items: center; justify-content: center;
    gap: 18px;
  }
  .brand {
    display: flex; align-items: center; gap: 10px;
    color: var(--gold); font-weight: 700; letter-spacing: 0.06em;
    text-transform: uppercase;
  }
  .brand-dot { width: 16px; height: 16px; border-radius: 50%; background: var(--gold); }
  .front-panel .brand { font-size: 22px; }
  .front-url { color: var(--muted-link); font-size: 14px; letter-spacing: 0.02em; }

  /* Back */
  .card--back {
    top: 475px;
    background:
      linear-gradient(160deg, transparent 30%, rgba(255,255,255,0.08) 45%, transparent 60%),
      linear-gradient(180deg, var(--card-royal-light), var(--card-royal));
  }
  .card--back .brand { position: absolute; top: 48px; right: 40px; font-size: 20px; }
  .back-rule {
    position: absolute; top: 112px; left: 250px; right: 40px;
    height: 1px; background: var(--rule);
  }
  .contact-list {
    position: absolute; top: 132px; right: 40px;
    list-style: none; text-align: right;
    color: var(--white); font-size: 14px; line-height: 24px;
  }
  .contact-list li { display: flex; justify-content: flex-end; align-items: center; gap: 10px; }
  .contact-list svg { width: 12px; height: 12px; fill: var(--gold); flex: none; }
  .holder { position: absolute; left: 48px; bottom: 70px; }
  .holder-name {
    color: var(--white); font-weight: 700; font-size: 28px;
    letter-spacing: 0.03em; text-transform: uppercase; margin-bottom: 6px;
  }
  .holder-role { color: var(--gold); font-size: 17px; line-height: 22px; }
</style>
</head>
<body>
<main class="canvas">
  <section class="card card--front" aria-label="Card front">
    <div class="front-panel">
      <div class="brand"><span class="brand-dot"></span>Brightline</div>
      <div class="front-url">www.brightlinecontrols.com</div>
    </div>
  </section>

  <section class="card card--back" aria-label="Card back">
    <div class="brand"><span class="brand-dot"></span>Brightline</div>
    <div class="back-rule"></div>
    <ul class="contact-list">
      <li>(800) 555-0142 X 20
        <svg viewBox="0 0 12 12"><path d="M2.5 1l2 2.2-1 1.3c.7 1.5 1.7 2.5 3 3.1l1.3-1 2.2 2-1.2 1.9C4.5 10 2 7.5 1 3.2z"/></svg></li>
      <li>(888) 555-0187
        <svg viewBox="0 0 12 12"><path d="M3 1h6v3H3zM1 5h10v4H9v2H3V9H1zM4 8v2h4V8z"/></svg></li>
      <li>mokafor@brightlinecontrols.com
        <svg viewBox="0 0 12 12"><path d="M1 2.5h10v7H1zM1.6 3l4.4 3.4L10.4 3z"/></svg></li>
      <li>www.brightlinecontrols.com
        <svg viewBox="0 0 12 12"><path d="M5 3.2l1.6-1.6a2.2 2.2 0 013.2 3.2L8.2 6.4 7.4 5.6l1.6-1.6A1 1 0 007.4 2.4L5.8 4zM7 8.8L5.4 10.4a2.2 2.2 0 01-3.2-3.2L3.8 5.6l.8.8L3 8a1 1 0 001.6 1.6L6.2 8zM4.2 7l2.8-2.8.8.8L5 7.8z"/></svg></li>
      <li>412 Harbor Lane Islandia, NY 11749
        <svg viewBox="0 0 12 12"><path d="M6 .8a3.8 3.8 0 013.8 3.8C9.8 7.4 6 11.2 6 11.2S2.2 7.4 2.2 4.6A3.8 3.8 0 016 .8zm0 2.2a1.6 1.6 0 100 3.2 1.6 1.6 0 000-3.2z"/></svg></li>
    </ul>
    <div class="holder">
      <h1 class="holder-name">Marlene Okafor</h1>
      <p class="holder-role">Quality Assurance Mgr</p>
      <p class="holder-role">QR5583 Representative</p>
    </div>
  </section>
</main>
</body>
</html>
```